Etiketten für Olivenöl-Intensivcreme
Zielgruppe
Wir produzieren Bio-Food, u.a. Wein und Olivenöl. Jetzt soll eine Olivenöl-Intensivcreme im Bereich Kosmetik auf dem Markt platziert werden. Unsere Zielgruppe hat ein sehr breites Altersspektrum (jung bis alt), ist naturverbunden, tierlieb, gebildet, kritisch-reflektierend, weiß gute Qualität zu schätzen, ist überwiegend weiblich. Die Olivenöl-Intensivcreme hat eine sehr breite Verwendung und soll sich als 'Allzweckwaffe' in jedem Haushalt etablieren (Babyhaut-Pflege, Lippenpflege, Ganzkörperpflege, Hand-Schutzcreme etc.).
Aufgabenstellung
Die Creme soll heißen: Tavunel (es könnte z.B. der Buchstabe 'O' durch eine Olive ersetzt werden). Es gibt zwei Etikette (Deckeloberseite der Metalldose und auf dem Boden). Der Durchmesser der Etikette ist jeweils 5,5 cm. Die Deckelunterseite gilt reinen Pflichtangaben. Im Dateidownloadbereich sind die Textvorgaben für die Etikette. MUT zur Farbe! Wir sind NICHT brav und angepasst! Orange kann Akzente setzen bzw. für Aufmerksamkeit im Regal sorgen.

```html
<!DOCTYPE html>
<html lang="de">
<head>
<meta charset="utf-8">
<title>Tavunel – Etiketten</title>
<link rel="stylesheet" href="https://fonts.googleapis.com/css2?family=Josefin+Sans:wght@300;400&family=Allura&family=Great+Vibes&display=swap">
<style>
  :root {
    --canvas: #d8d8d8;
    --label: #ffffff;
    --gold: #b08510;
    --gold-text: #b38b1c;
    --white: #ffffff;
  }
  * { box-sizing: border-box; margin: 0; padding: 0; }
  html, body { width: 1200px; height: 1200px; overflow: hidden; }
  body {
    background: var(--canvas);
    font-family: "Josefin Sans", sans-serif;
    font-variant: small-caps;
    position: relative;
  }
  .label {
    position: absolute;
    top: 330px;
    width: 540px;
    height: 540px;
    border-radius: 50%;
    background: var(--label);
    overflow: hidden;
    text-align: center;
  }
  .label--front { left: 35px; }
  .label--back { left: 625px; }

  .brand {
    position: absolute;
    left: 0; right: 0;
    top: 70px;
    color: var(--gold-text);
    font-size: 25px;
    line-height: 28px;
    font-variant: normal;
    letter-spacing: 0.5px;
  }
  .band {
    position: absolute;
    left: 0; right: 0;
    top: 110px;
    height: 290px;
    background: var(--gold);
    color: var(--white);
  }
  .band > * { position: absolute; left: 0; right: 0; }
  .pill-row { text-align: center; }
  .pill {
    display: inline-block;
    background: var(--white);
    color: var(--gold-text);
    border-radius: 16px;
    letter-spacing: 0.8px;
  }

  /* front */
  .product-name {
    top: 2px;
    font-family: "Allura", cursive;
    font-variant: normal;
    font-size: 160px;
    line-height: 160px;
  }
  .label--front .pill-row { top: 158px; }
  .label--front .pill { font-size: 29px; line-height: 32px; padding: 3px 22px 0; }
  .category { top: 194px; font-size: 32px; line-height: 34px; letter-spacing: 0.8px; }
  .claims {
    top: 232px;
    display: flex;
    justify-content: center;
    align-items: center;
    gap: 12px;
    font-family: "Great Vibes", cursive;
    font-variant: normal;
    font-size: 36px;
    line-height: 42px;
  }
  .claims .sprig {
    width: 56px; height: 42px;
    border-radius: 6px;
    background: rgba(255,255,255,0.55);
  }
  .purpose {
    position: absolute;
    top: 415px; left: 0; right: 0;
    color: var(--gold-text);
    font-size: 31px;
    line-height: 33px;
    letter-spacing: 1px;
  }

  /* back */
  .label--back .pill-row { top: 11px; }
  .label--back .pill { font-size: 22px; line-height: 24px; padding: 3px 14px 0; }
  .info { top: 43px; font-size: 23px; line-height: 25px; letter-spacing: 0.5px; }
  .info p + p { margin-top: 6px; }
  .info u { text-underline-offset: 2px; }
  .divider {
    top: 255px;
    left: 12px !important; right: 12px !important;
    border-top: 1px solid var(--white);
  }
  .best-before { top: 262px; font-size: 20px; line-height: 24px; letter-spacing: 0.3px; }
  .imprint {
    position: absolute;
    top: 411px;
    left: 0; right: 0;
    color: var(--gold-text);
    font-size: 19px;
    line-height: 21px;
    letter-spacing: 0.3px;
  }
  .recycle {
    position: absolute;
    top: 411px;
    left: 102px;
    width: 34px; height: 34px;
    border-radius: 50%;
    background: var(--gold-text);
  }
  .volume {
    position: absolute;
    top: 408px;
    left: 396px;
    width: 44px;
    color: var(--gold-text);
    font-size: 30px;
    line-height: 26px;
    text-align: center;
  }
  .volume small { display: block; font-size: 22px; line-height: 20px; }
</style>
</head>
<body>
  <section class="label label--front">
    <div class="brand">FERAVO.LAND</div>
    <div class="band">
      <div class="product-name">Tavunel</div>
      <div class="pill-row"><span class="pill">Olivenöl-Intensivcreme</span></div>
      <div class="category">Naturkosmetik</div>
      <div class="claims">
        <span>Bio-Olive</span>
        <span class="sprig" role="img" aria-label="Olivenzweig-Ornament"></span>
        <span>Vegan</span>
      </div>
    </div>
    <div class="purpose">Pflege- und<br>Schutzcreme</div>
  </section>

  <section class="label label--back">
    <div class="brand">FERAVO.LAND</div>
    <div class="band">
      <div class="pill-row"><span class="pill">wasserfreie Creme, unparfümiert</span></div>
      <div class="info">
        <p><u>Ingredients:</u> Olea Europaea Fruit Oil,<br>Hydrogenated Rapeseed Oil, Tocopherol</p>
        <p><u>Anwendung:</u> Sparsam auf die trockene<br>Haut auftragen (ergiebig!). Die Einwirkzeit<br>kann einige Minuten dauern, vorher kann es<br>beim Berühren von Gegenständen mit den<br>gecremten Körperpartien<br>zur Fettübertragung kommen.</p>
      </div>
      <div class="divider"></div>
      <div class="best-before">Mind. haltbar: Januar 2021 · Made in Germany</div>
    </div>
    <div class="recycle" role="img" aria-label="Recycling-Zeichen"></div>
    <div class="imprint">FERAVO.LAND<br>Dr. med. Marlene Bessel<br>Hafenweg 12 · D-24100 Kiel<br>www.feravo.land</div>
    <div class="volume">150<small>ml</small></div>
  </section>
</body>
</html>
```